Redesign of ademvrijwinkel.nl – Clean, Trustworthy & User-Friendly Medical Equipment We...

PLEASE DO NOT CONTACT US OUTSIDE PIXELVERBAND.COM

We are looking for a talented and creative web designer to redesign the website www.ademvrijwinkel.nl, a Dutch online store specializing in medical oxygen concentrators and related products.

The current website is functional but outdated in terms of design, structure, and user experience. We want a fresh, modern, and trustworthy design that reflects the medical and professional nature of the business, while also being clear, accessible, and easy to navigate for a broad audience — including elderly users and people with limited technical skills.

About the Business:
Ademvrijwinkel.nl provides high-quality oxygen concentrators and accessories for both home and mobile use. The target audience includes individuals with respiratory conditions, healthcare professionals, and caregivers. Trust, clarity, and ease of use are key.

What We’re Looking For:
A clean and modern layout with a medical/professional feel
Strong focus on usability and accessibility
A design that works flawlessly on desktop and mobile (responsive)
Clear product presentation and easy-to-use navigation
Use of calming colors (e.g. white, light blue, grey tones) that reflect a medical/healthcare environment
Clear call-to-actions (e.g. “Vraag een offerte aan”, “Neem contact op”, etc.)
A design that builds trust and encourages inquiries or purchases

Pages We Need Designed:
Homepage
Product overview page (category)
Product detail page

Inspiration / Style Examples:
We’re looking for something in the style of:

Norvalt Healthcare
Varoq.nl
Welzijnsteunwerk.nl
Quill (for clean layout and spacing)

Deliverables:
Full desktop and mobile designs (Figma, Adobe PS)
All source files and assets used (fonts, icons, images, etc.)
Clean and organized layers
Design must be ready for implementation by our development team

Target Market(s)

Ademvrijwinkel.nl targets both B2C and B2B audiences within the medical and healthcare sector in europe

Industry/Entity Type

Medical

Number of Pages Required

2 page

Font styles to use
Sans Serif

Requirements
Must have
• Clean and professional design, responsive layout (desktop and mobile), calming medical color scheme (e.g. light blue, white, grey), clear product presentation with specs and images, strong call-to-actions (e.g. "Vraag een offerte aan"), trust elements (certifications, reviews, support info), easy navigation for elderly and non-tech-savvy users, contact form easily accessible, SEO-friendly structure, fast loading design, privacy and regulatory compliance elements (e.g. CE mark info, medical disclaimers).
Should not have
• Overly complex design, dark or aggressive color schemes, small or hard-to-read fonts, cluttered layout, distracting animations, unnecessary pop-ups, autoplay videos or sounds, technical jargon without explanation, hidden contact options, slow-loading pages.

```html
<!DOCTYPE html>
<html lang="nl">
<head>
<meta charset="utf-8">
<title>Ademvrij – Ademvrijwinkel.nl</title>
<link href="https://fonts.googleapis.com/css2?family=Michroma&family=Poppins:wght@300;400;500;600&display=swap" rel="stylesheet">
<style>
:root{
  --blue:#5aaee3;
  --blue-soft:#e3f1fb;
  --blue-deep:#1d5fa6;
  --navy:#1f3554;
  --ink:#1a1a1a;
  --muted:#8a8f96;
  --line:#e6e9ee;
  --footer:#3b3b3b;
  --star:#f5a623;
  --white:#fff;
}
*{box-sizing:border-box;margin:0;padding:0}
html,body{width:1200px;height:4878px;overflow:hidden}
body{position:relative;background:var(--white);font-family:"Poppins",sans-serif;color:var(--ink)}
.abs{position:absolute}
.display{font-family:"Michroma",sans-serif;font-weight:400;color:var(--ink)}
a{color:inherit}

/* header */
.site-header{left:0;top:0;width:1200px;height:85px;background:var(--white);border-radius:0 0 18px 18px;z-index:3}
.brand{left:151px;top:22px;font-family:"Poppins",sans-serif;font-weight:600;font-size:30px;color:var(--navy);line-height:1.2}
.nav{left:340px;top:34px;display:flex;gap:26px;font-size:12px}
.btn{display:flex;align-items:center;justify-content:center;background:var(--blue);color:var(--white);font-size:13px;font-weight:500;border-radius:4px;text-decoration:none}
.header-cta{left:929px;top:23px;width:121px;height:41px}

/* hero */
.hero{left:0;top:85px;width:1200px;height:631px;background:linear-gradient(180deg,#cfe6f7 0%,#9fcff0 55%,#6db6ea 100%)}
.hero-photo{left:520px;top:85px;width:680px;height:700px;background:linear-gradient(135deg,#e8eef3 0%,#c9d6e0 45%,#8ea2b4 100%);border-radius:0 0 0 40px;opacity:.9}
.hero-fade{left:0;top:85px;width:760px;height:631px;background:linear-gradient(90deg,rgba(200,228,247,.95) 60%,rgba(200,228,247,0))}
.hero-title{left:151px;top:198px;font-size:52px}
.hero-sub{left:320px;top:284px;font-size:36px}
.hero-rule{left:151px;top:306px;width:152px;height:3px;background:var(--ink)}
.hero-text{left:151px;top:352px;width:440px;font-size:12px;line-height:21px}
.hero-get{left:151px;top:449px;width:92px;height:119px;background:#3f6f95;border-radius:8px;color:var(--white);font-size:13px;text-align:center;padding-top:46px;line-height:15px}
.stat-big{font-family:"Michroma",sans-serif;font-size:34px;line-height:1}
.stat-lbl{font-size:14px;line-height:17px;margin-top:6px}

/* section titles */
.h2{font-size:40px}
.h2c{left:0;width:1200px;text-align:center;font-size:42px;line-height:56px}

/* products */
.prod-card{top:962px;width:287px;height:296px;background:var(--blue-soft)}
.prod-img{position:absolute;inset:20px 40px;border-radius:16px}
.prod-title{font-size:18px;font-weight:500;line-height:22px;width:290px}
.prod-desc{font-size:10px;color:var(--muted);line-height:14px;width:280px;margin-top:8px}
.prod-link{font-size:14px;font-weight:500;text-decoration:underline;margin-top:12px;display:block}

/* features */
.feature{top:1624px;width:212px;height:203px;background:var(--white);border:1px solid var(--line);border-radius:6px;box-shadow:0 4px 12px rgba(0,0,0,.08);text-align:center;padding:30px 8px 0}
.feature svg{width:88px;height:80px}
.feature h3{font-size:15px;font-weight:500;margin-top:12px}
.feature p{font-size:9.5px;line-height:13px;margin-top:10px}
.feature.active{background:var(--blue);color:var(--white);border-color:var(--blue)}

/* popular */
.popular{left:0;top:1921px;width:1200px;height:674px;background:linear-gradient(120deg,#70b8ea 0%,#bfe0f6 60%,#e0f0fb 100%)}
.pop-card{top:2061px;width:286px;height:383px;background:var(--white);border-radius:6px;overflow:hidden}
.pop-img{height:188px;background:linear-gradient(135deg,#dfe6ea,#a9b7c1)}
.pop-body{padding:16px 15px}
.pop-body h3{font-size:18px;font-weight:500}
.pop-body .d{font-size:10px;color:var(--muted);line-height:15px;margin-top:8px}
.price-row{display:flex;justify-content:space-between;margin-top:14px}
.price{font-size:20px;font-weight:500}
.rating{font-size:10px;text-align:right}
.stars{color:var(--star);font-size:13px;letter-spacing:2px}
.cart-row{display:flex;justify-content:space-between;align-items:center;margin-top:14px}
.cart{font-size:13px;font-weight:500;text-decoration:underline}
.plus{width:28px;height:28px;background:#111;color:var(--white);border-radius:4px;display:flex;align-items:center;justify-content:center;font-size:18px}
.quote-btn{left:505px;top:2500px;width:218px;height:41px;background:var(--white);color:var(--ink);border-radius:4px}

/* providing */
.prov-photo{left:151px;top:2690px;width:595px;height:396px;background:linear-gradient(135deg,#eef1f3,#c7d1d8)}
.prov-panel{left:606px;top:2711px;width:444px;height:354px;background:var(--white);box-shadow:0 4px 16px rgba(0,0,0,.12);padding:24px 22px}
.prov-panel h2{font-size:29px;line-height:50px;white-space:nowrap}
.ticks{list-style:none;margin-top:10px}
.ticks li{display:flex;align-items:center;gap:12px;font-size:12px;height:31px}
.ticks svg{width:15px;height:15px;flex:none}
.learn{width:120px;height:41px;margin-top:18px}

/* stats */
.num{top:3160px;font-family:"Michroma",sans-serif;font-size:40px;color:var(--blue-deep);line-height:1}
.num-lbl{top:3207px;font-size:13px}

/* testimonials */
.t-side{top:3487px;width:146px;height:159px;background:#c7ccd2;border-radius:4px}
.t-main{left:380px;top:3438px;width:441px;height:240px;background:#7cc0ec;border-radius:6px;color:var(--white);text-align:center;padding:50px 34px 0}
.avatar{left:567px;top:3393px;width:66px;height:66px;border-radius:50%;background:linear-gradient(135deg,#d4c2b3,#8a7c72);border:3px solid var(--white);z-index:2}
.t-main .n{font-size:14px}
.t-main .r{font-size:10px;margin-top:2px}
.t-main p{font-size:11px;line-height:17px;margin-top:14px}
.t-main .stars{color:var(--white);margin-top:8px;font-size:16px}
.qmark{font-family:"Michroma",sans-serif;font-size:34px;line-height:1}

/* contact */
.contact-photo{left:151px;top:3852px;width:311px;height:525px;background:linear-gradient(160deg,#9fb6c8,#4f6a80)}
.contact-form{left:462px;top:3852px;width:588px;height:525px;background:var(--white);box-shadow:0 2px 12px rgba(0,0,0,.1);padding:40px 43px}
.contact-form h2{font-size:28px;font-weight:300;color:#555}
.field label{display:block;font-size:12px;color:#555;margin:18px 0 10px 4px}
.field div{height:41px;border:1px solid #cfd4da;border-radius:6px}
.submit{height:54px;margin-top:28px;font-size:15px;border-radius:4px}

/* footer */
.site-footer{left:0;top:4471px;width:1200px;height:407px;background:var(--footer);color:var(--white)}
.foot-brand{left:151px;top:4560px;font-family:"Poppins",sans-serif;font-weight:600;font-size:60px;color:var(--blue);line-height:1.2}
.foot-text{left:151px;top:4668px;width:360px;font-size:14px;line-height:24px;color:var(--white)}
.social{top:4736px;width:31px;height:31px;border-radius:50%;background:var(--white)}
.foot-col h4{font-size:18px;font-weight:500;margin-bottom:14px}
.foot-col a{display:block;font-size:11.5px;text-decoration:none;line-height:30px}
.foot-rule{left:76px;top:4810px;width:974px;height:1px;background:#777}
.foot-small{top:4828px;font-size:11px;color:#ddd}
</style>
</head>
<body>

<header class="abs site-header">
  <div class="abs brand">Ademvrij</div>
  <nav class="abs nav"><span>Home</span><span>About Us</span><span>CATEGORIES</span><span>FEATURED</span><span>WHY CHOOSE US</span><span>Testimonials</span></nav>
  <a class="abs btn header-cta">Contact Us</a>
</header>

<section>
  <div class="abs hero"></div>
  <div class="abs hero-photo" role="img" aria-label="Caregiver with an elderly couple beside portable oxygen concentrators"></div>
  <div class="abs hero-fade"></div>
  <h1 class="abs display hero-title">Breathe Easy</h1>
  <div class="abs hero-rule"></div>
  <div class="abs display hero-sub">Live Better</div>
  <p class="abs hero-text">Lorem Ipsum Dolor Sit Amet Consectetur. Mauris Enim Dapibus Mauris Leo Senectus. Penatibus Enim Aenean Pretium Tortor Ut Id Eget Nisl. Erat Enim Venenati</p>
  <a class="abs hero-get">Get ↗<br>Started</a>
  <div class="abs" style="left:282px;top:474px"><div class="stat-big">99%</div><div class="stat-lbl">Clients<br>Satisfaction</div></div>
  <div class="abs" style="left:413px;top:520px"><div class="stat-big">100%</div><div class="stat-lbl">Experienced &amp;<br>Dedicated Staff</div></div>
</section>

<section>
  <h2 class="abs display h2" style="left:151px;top:858px">Our Products</h2>
  <a class="abs btn" style="left:848px;top:857px;width:202px;height:53px;font-size:14px">View All Categories</a>

  <div class="abs prod-card" style="left:151px"><div class="prod-img" role="img" aria-label="Stationary oxygen concentrator" style="background:linear-gradient(135deg,#cfe2ef,#8fb2c9)"></div></div>
  <div class="abs prod-card" style="left:456px"><div class="prod-img" role="img" aria-label="Portable oxygen concentrator on wheels" style="background:linear-gradient(135deg,#5a5f66,#1f2226)"></div></div>
  <div class="abs prod-card" style="left:763px"><div class="prod-img" role="img" aria-label="Oxygen mask with green tubing" style="background:linear-gradient(135deg,#dcefe4,#5f9c79)"></div></div>

  <div class="abs" style="left:151px;top:1282px"><div class="prod-title">OXYGEN CONCENTRATORS</div><p class="prod-desc">Lorem ipsum dolosit ametlorem ipsum dolosit ametlorem ipsum dolosit ametlorem ipsum dolosit amet</p><a class="prod-link">Bekijk producten</a></div>
  <div class="abs" style="left:456px;top:1275px"><div class="prod-title">PORTABLE OXYGEN<br>CONCENTRATORS</div><p class="prod-desc">Lorem ipsum dolosit ametlorem ipsum dolosit ametlorem ipsum dolosit ametlorem ipsum dolosit amet</p><a class="prod-link">Bekijk producten</a></div>
  <div class="abs" style="left:763px;top:1282px"><div class="prod-title">ACCESSORIES</div><p class="prod-desc">Lorem ipsum dolosit ametlorem ipsum dolosit ametlorem ipsum dolosit ametlorem ipsum dolosit amet</p><a class="prod-link">Bekijk producten</a></div>
</section>

<section>
  <h2 class="abs display h2c" style="top:1478px">Waarom Kiezen Voor<br>Ademvrijwinkel.Nl</h2>

  <div class="abs feature" style="left:151px">
    <svg viewBox="0 0 88 80" fill="none" stroke="#2f86c8" stroke-width="2"><rect x="14" y="22" width="60" height="54"/><rect x="30" y="6" width="28" height="20"/><path d="M44 10v12M38 16h12"/><rect x="38" y="56" width="12" height="20"/><rect x="20" y="32" width="8" height="8"/><rect x="60" y="32" width="8" height="8"/><rect x="20" y="48" width="8" height="8"/><rect x="60" y="48" width="8" height="8"/></svg>
    <h3>High-Quality Devices</h3><p>CE Certified Oxygen Concentrators Meeting European Medical Standards</p>
  </div>
  <div class="abs feature" style="left:380px">
    <svg viewBox="0 0 88 80" fill="none" stroke="#2f86c8" stroke-width="2"><circle cx="30" cy="18" r="9"/><circle cx="58" cy="18" r="9"/><path d="M16 76V42q0-12 14-12t14 12v34M44 76V42q0-12 14-12t14 12v34"/></svg>
    <h3>Easy To Use</h3><p>Simple And Intuitive Design Suitable For Elderly And Non-Tech-Savvy Users</p>
  </div>
  <div class="abs feature active" style="left:609px">
    <svg viewBox="0 0 88 80" fill="none" stroke="#fff" stroke-width="2"><circle cx="44" cy="40" r="34"/><circle cx="44" cy="32" r="9"/><path d="M28 60q16-18 32 0"/></svg>
    <h3>Expert Guidance</h3><p>Our Specialists Help You Choose The Right Oxygen Concentrator For Your Needs</p>
  </div>
  <div class="abs feature" style="left:838px">
    <svg viewBox="0 0 88 80" fill="none" stroke="#2f86c8" stroke-width="2"><circle cx="32" cy="16" r="9"/><path d="M18 76V44q0-12 14-12t14 10"/><rect x="46" y="40" width="28" height="26"/><path d="M46 50h28M60 40v10"/></svg>
    <h3>Fast &amp; Reliable Delivery</h3><p>Quick Shipping Across Europe So You Can Start Using Your Device Without Delay</p>
  </div>
</section>

<section>
  <div class="abs popular"></div>
  <h2 class="abs display h2c" style="top:1963px">Populaire Oxygen Concentrators</h2>

  <article class="abs pop-card" style="left:165px">
    <div class="pop-img" role="img" aria-label="Smiling senior man beside a home oxygen concentrator"></div>
    <div class="pop-body"><h3>LUMENO AIRFLO</h3><p class="d">Premium Tattoo Machines, Needles, Inks &amp; Supplies For Beginners To Pro Artists</p>
      <div class="price-row"><span class="price">$20</span><div class="rating">4.5 Reating<div class="stars">★★★★★</div></div></div>
      <div class="cart-row"><span class="cart">ADD TO CART</span><span class="plus">+</span></div></div>
  </article>
  <article class="abs pop-card" style="left:471px">
    <div class="pop-img" role="img" aria-label="Man seated next to a white oxygen concentrator" style="background:linear-gradient(135deg,#dde8d8,#9fb39a)"></div>
    <div class="pop-body"><h3>LUMENO AIRFLO</h3><p class="d">Premium Tattoo Machines, Needles, Inks &amp; Supplies For Beginners To Pro Artists</p>
      <div class="price-row"><span class="price">$20</span><div class="rating">4.5 Reating<div class="stars">★★★★★</div></div></div>
      <div class="cart-row"><span class="cart">ADD TO CART</span><span class="plus">+</span></div></div>
  </article>
  <article class="abs pop-card" style="left:778px">
    <div class="pop-img" role="img" aria-label="Nurse assisting a patient using an oxygen concentrator" style="background:linear-gradient(135deg,#e4ebef,#8fb0c6)"></div>
    <div class="pop-body"><h3>LUMENO AIRFLO</h3><p class="d">Premium Tattoo Machines, Needles, Inks &amp; Supplies For Beginners To Pro Artists</p>
      <div class="price-row"><span class="price">$20</span><div class="rating">4.5 Reating<div class="stars">★★★★★</div></div></div>
      <div class="cart-row"><span class="cart">ADD TO CART</span><span class="plus">+</span></div></div>
  </article>

  <a class="abs btn quote-btn">Request A Quote</a>
</section>

<section>
  <div class="abs prov-photo" role="img" aria-label="Elderly man with nasal cannula seated beside an oxygen concentrator"></div>
  <div class="abs prov-panel">
    <h2 class="display">Providing<br>Reliable Oxygen</h2>
    <ul class="ticks">
      <li><svg viewBox="0 0 16 16"><circle cx="8" cy="8" r="8" fill="#111"/><path d="M4.5 8.2l2.3 2.3 4.7-4.8" stroke="#fff" stroke-width="1.8" fill="none"/></svg>How To Fill The Form Online Or In-Person</li>
      <li><svg viewBox="0 0 16 16"><circle cx="8" cy="8" r="8" fill="#111"/><path d="M4.5 8.2l2.3 2.3 4.7-4.8" stroke="#fff" stroke-width="1.8" fill="none"/></svg>How To Book Appointments</li>
      <li><svg viewBox="0 0 16 16"><circle cx="8" cy="8" r="8" fill="#111"/><path d="M4.5 8.2l2.3 2.3 4.7-4.8" stroke="#fff" stroke-width="1.8" fill="none"/></svg>What To Do Before Consultations</li>
      <li><svg viewBox="0 0 16 16"><circle cx="8" cy="8" r="8" fill="#111"/><path d="M4.5 8.2l2.3 2.3 4.7-4.8" stroke="#fff" stroke-width="1.8" fill="none"/></svg>How To Submit Consent Forms Or Patient Agreements</li>
    </ul>
    <a class="btn learn">Learn More</a>
  </div>
</section>

<section>
  <div class="abs num" style="left:151px">2000+</div><div class="abs num-lbl" style="left:151px">CE Certified Medical Devices</div>
  <div class="abs num" style="left:427px">150+</div><div class="abs num-lbl" style="left:401px">Fast Shipping Across Europe</div>
  <div class="abs num" style="left:660px">1500+</div><div class="abs num-lbl" style="left:649px">Trusted By Healthcare Experts</div>
  <div class="abs num" style="left:927px">50+</div><div class="abs num-lbl" style="left:905px">24/7 Customer Support</div>
</section>

<section>
  <h2 class="abs display h2c" style="top:3304px">Wat Onze Klanten Zeggen</h2>
  <div class="abs t-side" style="left:235px"><div class="qmark" style="color:#fff;margin:26px 0 0 14px;font-size:22px">“</div></div>
  <div class="abs t-side" style="left:821px"><div class="qmark" style="color:#fff;margin:110px 0 0 112px;font-size:22px">”</div></div>
  <div class="abs avatar" role="img" aria-label="Customer portrait"></div>
  <div class="abs t-main">
    <div class="n">Jesse Vermeer</div><div class="r">Global Directives Architect</div>
    <div class="qmark abs" style="left:22px;top:46px">“</div>
    <p>Lorem ipsum dolor sit amet consectetur. Velit ultricies et faucibus tortor suspendisse id auctor. Integer commodo eget at nec nisl amet. Rhoncus egestas pharetra mi ipsum. Tellus vestibulum justo nibh neque pulvinar congue. Laoreet eu placerat cursus sed nunc. Est lectus amet rhoncus ultricies augue faucibus egestas sit volutpat. Porttitor velit urna amet in dictum ut sapien.</p>
    <div class="stars">★★★★<span style="opacity:.5">★</span></div>
    <div class="qmark abs" style="right:22px;top:190px">”</div>
  </div>
</section>

<section>
  <h2 class="abs display h2c" style="top:3760px">Heeft U Advies Nodig</h2>
  <div class="abs contact-photo" role="img" aria-label="Nurse in a face mask helping a patient with an oxygen mask"></div>
  <form class="abs contact-form">
    <h2>Contact Us</h2>
    <div class="field"><label>Name</label><div></div></div>
    <div class="field"><label>Email</label><div></div></div>
    <div class="field"><label>Addess</label><div></div></div>
    <div class="field"><label>Phone Number</label><div></div></div>
    <div class="btn submit">Submit</div>
  </form>
</section>

<footer class="abs site-footer"></footer>
<div class="abs foot-brand">Ademvrij</div>
<p class="abs foot-text">Lorem Ipsum Dolor Amet Consectetur. Mauris Enim Dapibus Mauris Leo</p>
<div class="abs social" style="left:151px" aria-label="Social link"></div>
<div class="abs social" style="left:202px" aria-label="Social link"></div>
<div class="abs social" style="left:252px" aria-label="Social link"></div>
<div class="abs social" style="left:302px" aria-label="Social link"></div>
<div class="abs foot-col" style="left:723px;top:4530px;color:#fff">
  <h4>Used Full Links</h4><a>Home</a><a>about Us</a><a>Categories</a><a>Featured</a><a>Why Choose us</a><a>Testimonials</a><a>contact us</a>
</div>
<div class="abs foot-col" style="left:969px;top:4530px;color:#fff">
  <h4>Legal</h4><a>Terms Of Use</a><a>Privacy Policy</a><a>Cookie Policy</a>
</div>
<div class="abs foot-rule"></div>
<div class="abs foot-small" style="left:76px">Copyright © 2025 All Right Reserved</div>
<div class="abs foot-small" style="left:727px">Privacy Policy</div>
<div class="abs foot-small" style="left:833px">Terms Of Service</div>
<div class="abs foot-small" style="left:957px">Cookies Settings</div>

</body>
</html>
```